HIDE WARDEN

Labels for Men's Skin Care. Organic, target 25-35 The label will be 2x3.5 on a 4oz amber bottle. 3 labels with the information shown on the uploaded sample.
Our product is a e-commerce built to help my 24 year old twin sons have a business of their own. Although it will be sold online they will also do foot work and sell to barbers at barber shops using as a mist on customers after shaving. So we want something that will attract male customers and will look good in a modern Barbershop. This is there shot and packaging is very very important. So if you could help us out with a great label we would be working with you in the future for package design. Our line will have several mens Organic natural skin care cleanser, mask toners and moisturizers..Thank you for your help. We also hope to put our products in beauty supply shops. So it needs to stand out as a mans product but still be traditional male product. Oh be creative mind that you are and remember we are trying to build a brand that attracts 25-35 male. Thank you

Hello, I just wanted to let you know that I am up working very late.

for anyone on the other side of the world up and working. I sleep about
3 hours.. So I'll be up for a few more hours and then up again around 5am my time

Good morning... I just wanted to say I will need three labels.. The words on all three are not that different and will fit pretty much the same on all three. So if you could work with one showing how the colors might be a little different on the other two you can do that with just the one label Just to make it easier on you if you like.. we can fix the other two once I find the right label,  Thank you it is 3am here.. still working.. I love it.

Target Market(s)

MALE 25-35

Industry/Entity Type

E-Commerce

Requirements
Must have
• final design must be fitted to the dieline uploaded.

```html
<!DOCTYPE html>
<html lang="en">
<head>
<meta charset="utf-8">
<title>Hide Warden – Daily Shave Fix Label</title>
<link rel="stylesheet" href="https://fonts.googleapis.com/css2?family=Montserrat:wght@300;400;700;800&family=Tinos&display=swap">
<style>
  :root {
    --ink: #000000;
    --white: #ffffff;
    --green: #3fb51a;
    --green-bright: #4fd11f;
    --green-deep: #1f5a0c;
    --leather-dark: #0d0d0d;
    --leather-mid: #2b2b2b;
  }
  * { margin: 0; padding: 0; box-sizing: border-box; }
  html, body { width: 686px; height: 1200px; overflow: hidden; background: var(--ink); }
  .label {
    position: relative;
    width: 686px;
    height: 1200px;
    background: var(--ink);
    font-family: "Montserrat", sans-serif;
    color: var(--white);
    overflow: hidden;
  }
  .leather-header {
    position: absolute; left: 0; top: 0; width: 686px; height: 311px;
    background: radial-gradient(ellipse at 50% 20%, var(--leather-mid) 0%, #1c1c1c 55%, var(--leather-dark) 100%);
  }
  .brand {
    position: absolute; left: 32px; top: 128px;
    display: flex; align-items: center; gap: 18px;
  }
  .brand-mark {
    width: 26px; height: 26px; background: var(--green);
  }
  .brand-name {
    font-weight: 400; font-size: 58px; line-height: 1;
    color: var(--white); letter-spacing: 2px;
  }
  .tagline {
    position: absolute; right: 23px; top: 214px;
    font-weight: 300; font-size: 30px; line-height: 1;
    letter-spacing: 5px; color: var(--white);
  }
  .accent-band {
    position: absolute; left: 0; top: 311px; width: 686px; height: 38px;
    background: linear-gradient(90deg, var(--green-deep) 0%, var(--green) 45%, var(--green-bright) 60%, var(--green) 80%, var(--green-deep) 100%);
  }
  .audience {
    position: absolute; left: 30px; top: 425px;
    font-weight: 800; font-size: 63px; line-height: 1; color: var(--green);
  }
  .product-title {
    position: absolute; left: 30px; top: 494px;
    font-weight: 700; font-size: 53px; line-height: 60px; color: var(--white);
  }
  .product-title .plus { color: var(--green); }
  .ingredient-note {
    position: absolute; left: 30px; top: 684px;
    font-weight: 400; font-size: 32px; line-height: 1; color: var(--green);
  }
  .fade-stripes { position: absolute; left: 0; top: 726px; }
  .side-note {
    position: absolute; left: 644px; top: 857px;
    transform: translate(-50%, -50%) rotate(-90deg);
    white-space: nowrap;
    font-weight: 400; font-size: 30px; line-height: 1; color: var(--green);
  }
  .flavour {
    position: absolute; left: 0; width: 686px; top: 1103px; text-align: center;
    font-weight: 800; font-size: 36px; line-height: 1; color: var(--white); letter-spacing: 0.5px;
  }
  .flavour .plus { color: var(--green); }
  .volume {
    position: absolute; left: 0; width: 686px; top: 1153px; text-align: center;
    font-family: "Tinos", serif; font-size: 27px; line-height: 1; color: var(--green);
  }
</style>
</head>
<body>
  <main class="label">
    <div class="leather-header" role="img" aria-label="Dark black leather texture background"></div>
    <div class="brand">
      <span class="brand-mark"></span>
      <span class="brand-name">HIDE WARDEN</span>
    </div>
    <div class="tagline">DAILY SHAVE FIX</div>

    <div class="accent-band"></div>

    <h1 class="audience">MEN’S</h1>
    <p class="product-title">Facial Conditioner<span class="plus">+</span><br>Calms Razor Burn<br>After Shaving</p>
    <p class="ingredient-note">with Botanical Healing Mint</p>

    <svg class="fade-stripes" width="620" height="300" viewBox="0 0 620 300" aria-hidden="true">
      <g fill="#3fb51a">
        <rect x="0" y="0" width="617" height="6" opacity="1"/>
        <rect x="0" y="14" width="617" height="6" opacity="0.95"/>
        <rect x="0" y="28" width="617" height="5" opacity="0.9"/>
        <rect x="0" y="42" width="617" height="5" opacity="0.84"/>
        <rect x="0" y="56" width="617" height="5" opacity="0.78"/>
        <rect x="0" y="70" width="617" height="5" opacity="0.72"/>
        <rect x="0" y="84" width="617" height="4" opacity="0.65"/>
        <rect x="0" y="98" width="617" height="4" opacity="0.58"/>
        <rect x="0" y="112" width="617" height="4" opacity="0.51"/>
        <rect x="0" y="126" width="617" height="4" opacity="0.45"/>
        <rect x="0" y="140" width="617" height="3" opacity="0.39"/>
        <rect x="0" y="154" width="617" height="3" opacity="0.33"/>
        <rect x="0" y="168" width="617" height="3" opacity="0.27"/>
        <rect x="0" y="182" width="617" height="3" opacity="0.22"/>
        <rect x="0" y="196" width="617" height="3" opacity="0.17"/>
        <rect x="0" y="210" width="617" height="2" opacity="0.13"/>
        <rect x="0" y="224" width="617" height="2" opacity="0.1"/>
        <rect x="0" y="238" width="617" height="2" opacity="0.07"/>
        <rect x="0" y="252" width="617" height="2" opacity="0.05"/>
        <rect x="0" y="266" width="617" height="2" opacity="0.03"/>
        <rect x="0" y="280" width="617" height="2" opacity="0.02"/>
      </g>
    </svg>

    <div class="side-note">Smooth Skin Blend</div>

    <p class="flavour">CRANBERRY <span class="plus">+</span> POMEGRANATE</p>
    <p class="volume">3.5 fl. oz 103ml</p>
  </main>
</body>
</html>
```